Lighting Product Brochure Design

We need a brochure templete design for a new LED public lighting product range. Products are called 'Quorivanta'.

We would like to see designs that are professional, simple, and impressive. Light color schemes are preferred. The finished design is preferably an editable template used within Word processors.

Basic product specification, logo and pictures enclosed. There will be not restriction on how the specification is presented in the brochure as long as it serves the purpose. A brochure sample has also been uploaded for reference only.

Please find short video footage to show you some of our projects in New Zealand:

https://files.vexamoor.net/item/q7Rm2KxwPz8Ld5NbTc4YhGs3VfJe9Ua6M/open?mode=public

Target Market(s)

Contractors, Councils, Private Utilities Companies.

Industry/Entity Type

Lighting Fixture

Font styles to use
Sans Serif

Requirements
Must have
• Product specificaiton, charts, drawings/pictures.

```html
<!DOCTYPE html>
<html lang="en">
<head>
<meta charset="utf-8">
<title>Quorivanta LED Public Lighting Brochure</title>
<link href="https://fonts.googleapis.com/css2?family=Montserrat:wght@300;400;600;700;800;900&family=Open+Sans:wght@400;600;700&display=swap" rel="stylesheet">
<style>
:root{
  --orange:#f26a21;
  --orange-dark:#d9531a;
  --tint:#fde6d4;
  --ink:#333333;
  --grey:#8a8a8a;
  --line:#e2e2e2;
  --row:#f3f3f3;
  --paper:#ffffff;
  --backdrop:#a2a2a2;
  --photo-a:#e9ecef;
  --photo-b:#c9ced4;
}
*{box-sizing:border-box;margin:0;padding:0}
html,body{width:1200px;height:4000px;overflow:hidden}
body{background:var(--backdrop);font-family:"Open Sans",Arial,sans-serif;color:var(--ink)}
.board{width:1200px;height:4000px;display:flex;flex-direction:column;justify-content:space-evenly;align-items:center}
.spread{display:flex;width:1120px;height:792px;box-shadow:0 10px 30px rgba(0,0,0,.25)}
.covers{gap:0}
.page{position:relative;width:560px;height:792px;background:var(--paper);overflow:hidden}
.spread .page.left{box-shadow:inset -14px 0 18px -14px rgba(0,0,0,.25)}
.spread .page.right{box-shadow:inset 14px 0 18px -14px rgba(0,0,0,.25)}

.brand{font-family:"Montserrat",Arial,sans-serif;font-weight:800;color:var(--ink);letter-spacing:.5px;display:inline-flex;align-items:center;gap:8px}
.brand .dot{width:10px;height:10px;background:var(--orange);display:inline-block}

.photo{background:linear-gradient(160deg,var(--photo-a),var(--photo-b));border-radius:4px}

/* front cover */
.front .brand{position:absolute;top:40px;right:44px;font-size:34px}
.front .hero{position:absolute;top:110px;left:44px;width:472px;height:260px}
.front .band{position:absolute;top:420px;left:-60px;width:700px;height:250px;background:var(--orange);transform:rotate(-14deg);transform-origin:center;padding:26px 0 0 120px}
.front .band h1{font-family:"Montserrat",Arial,sans-serif;font-weight:900;color:#fff;font-size:31px;line-height:1.05;text-transform:uppercase}
.front .band .thumbs{display:flex;gap:14px;margin-top:22px}
.front .band .thumb{width:140px;height:100px;border:4px solid #fff}
.front .url{position:absolute;bottom:82px;right:60px;transform:rotate(-14deg);font-family:"Montserrat",Arial,sans-serif;font-size:14px;letter-spacing:4px;color:var(--grey)}

/* back cover */
.back .stripes{position:absolute;inset:0}
.back .contact{position:absolute;left:60px;top:430px}
.back .brand{font-size:30px;margin-bottom:12px}
.back .phone{font-family:"Montserrat",Arial,sans-serif;font-size:28px;font-weight:600;display:flex;align-items:center;gap:10px}
.back .line{font-size:15px;display:flex;align-items:center;gap:10px;margin-top:6px}
.icon{width:18px;height:18px;flex:none}
.back .badges{display:flex;gap:16px;margin-top:26px}
.badge{width:34px;height:34px;background:#555;border-radius:6px}
.badge.round{border-radius:50%;background:#fff;border:2px solid #777}

/* inner pages */
.inner{padding:50px 46px}
.heading{font-family:"Montserrat",Arial,sans-serif;font-size:24px;text-transform:uppercase;color:var(--grey);font-weight:300;margin-bottom:16px}
.heading b{color:var(--orange);font-weight:800}
.notice{list-style:none;font-size:10.5px;line-height:1.5;color:#555}
.notice li{display:flex;gap:10px;margin-bottom:8px}
.notice li::before{content:"";width:10px;height:10px;border-radius:50%;background:var(--orange);flex:none;margin-top:3px}
.box{border:1.5px solid var(--orange);border-radius:10px;padding:8px 10px}
table{border-collapse:collapse;width:100%}
.ratings th{font-family:"Montserrat",Arial,sans-serif;color:var(--orange);font-size:10px;font-weight:700;text-align:left;padding:4px 3px;line-height:1.15}
.ratings td{font-size:10.5px;padding:5px 3px;border-top:1px solid var(--line)}
.ratings td:first-child{font-weight:700}
.footer-brand{position:absolute;left:46px;bottom:38px;font-size:20px}
.page-tab{position:absolute;right:0;bottom:40px;background:var(--orange);color:#fff;font-family:"Montserrat",Arial,sans-serif;font-size:11px;font-weight:600;padding:5px 16px 5px 20px;border-radius:14px 0 0 14px}
.footer-url{position:absolute;left:46px;bottom:44px;font-size:11px;font-weight:700;color:var(--ink)}

.nomen td{font-size:10.5px;padding:5px 4px;text-align:center;border:1px solid var(--line)}
.nomen td:first-child{text-align:left;font-weight:700;border:none}
.legend td{font-size:10.5px;padding:6px 6px;border-bottom:1px solid var(--line);vertical-align:top}
.legend td:first-child{width:60px;font-weight:700;text-align:center}
.legend th{font-size:10.5px;text-align:left;padding:6px;background:var(--row)}
.types{display:flex;gap:14px;margin-top:8px}
.type{flex:1}
.type p{font-family:"Montserrat",Arial,sans-serif;font-size:11px;color:var(--grey);margin-bottom:6px}
.type .chart{height:118px;border:1px solid var(--line);background:linear-gradient(180deg,#eef4fb,#f9f3e9)}

.corner{position:absolute;top:0;left:0}
.model{font-family:"Montserrat",Arial,sans-serif;font-size:26px;font-weight:800;color:var(--ink);padding-bottom:6px;border-bottom:3px solid var(--orange);display:inline-block;margin-bottom:12px}
.sub{font-family:"Montserrat",Arial,sans-serif;font-size:11px;font-weight:700;margin-bottom:8px;text-transform:uppercase}
.sub span{color:var(--orange)}
.spec td{font-size:9.5px;padding:4.6px 6px;border-bottom:1px solid #fff;vertical-align:top}
.spec td.k{background:var(--row);font-weight:700;text-transform:uppercase;width:150px;font-size:9px}
.spec td.d{background:#fafafa;color:#555}
.spec td.v{background:var(--tint);font-weight:600;width:95px}
.photos-title{font-family:"Montserrat",Arial,sans-serif;font-size:11px;font-weight:700;margin:16px 0 10px}
.photo-row{display:flex;gap:16px}
.photo-row .photo{flex:1;height:150px}
</style>
</head>
<body>
<main class="board">

  <!-- covers -->
  <section class="spread covers">
    <article class="page back">
      <svg class="stripes" viewBox="0 0 560 792" width="560" height="792" aria-hidden="true">
        <polygon points="440,0 470,0 560,120 560,160" fill="var(--orange)"/>
        <polygon points="480,0 520,0 560,60 560,110" fill="#cfcfcf"/>
        <polygon points="520,200 560,240 560,520 520,480" fill="var(--orange)"/>
        <polygon points="500,260 515,275 515,600 500,585" fill="#bdbdbd"/>
        <rect x="548" y="0" width="12" height="792" fill="#e6e6e6"/>
      </svg>
      <div class="contact">
        <div class="brand"><span class="dot"></span>Quorivanta</div>
        <div class="phone">
          <svg class="icon" viewBox="0 0 24 24"><path d="M6.6 10.8a15 15 0 006.6 6.6l2.2-2.2a1 1 0 011-.25 11 11 0 003.6.6 1 1 0 011 1V20a1 1 0 01-1 1A17 17 0 013 4a1 1 0 011-1h3.5a1 1 0 011 1 11 11 0 00.6 3.6 1 1 0 01-.25 1z" fill="var(--orange)"/></svg>
          0198 765 432
        </div>
        <div class="line">
          <svg class="icon" viewBox="0 0 24 24"><rect x="3" y="5" width="18" height="14" rx="2" fill="var(--orange)"/><path d="M3 7l9 6 9-6" stroke="#fff" stroke-width="2" fill="none"/></svg>
          info@quorivanta.com
        </div>
        <div class="line">
          <svg class="icon" viewBox="0 0 24 24"><circle cx="12" cy="12" r="9" fill="var(--orange)"/><path d="M3 12h18M12 3c3 3 3 15 0 18M12 3c-3 3-3 15 0 18" stroke="#fff" stroke-width="1.5" fill="none"/></svg>
          www.quorivanta.com
        </div>
        <div class="badges">
          <span class="badge"></span><span class="badge"></span><span class="badge"></span><span class="badge round"></span>
        </div>
      </div>
    </article>

    <article class="page front">
      <div class="brand"><span class="dot"></span>Quorivanta</div>
      <div class="photo hero" role="img" aria-label="Three white LED street luminaires of increasing size, viewed from below"></div>
      <div class="band">
        <h1>LED Public Lighting<br>Product Range</h1>
        <div class="thumbs">
          <div class="photo thumb" role="img" aria-label="Street luminaire mounted on pole arm"></div>
          <div class="photo thumb" role="img" aria-label="Street luminaire side view"></div>
          <div class="photo thumb" role="img" aria-label="Street luminaire angled view"></div>
        </div>
      </div>
      <div class="url">www.quorivanta.com</div>
    </article>
  </section>

  <!-- pages 01-02 -->
  <section class="spread">
    <article class="page left inner">
      <h2 class="heading"><b>Important</b> Notice</h2>
      <ul class="notice">
        <li>To reduce the risk of electric shock, disconnect power supply before installation or servicing.</li>
        <li>This product must be installed in accordance with the local electrical code. If you are not familiar with the codes, consult a qualified electrician.</li>
        <li>If a photo control receptacle is installed, use only rated controls listed for outdoor use.</li>
        <li>Luminaire must be securely fastened to the mounting arm; torque all bolts to the values given.</li>
        <li>The light source in this luminaire shall only be replaced by the maker or a service agent.</li>
      </ul>
      <h2 class="heading" style="margin-top:20px"><b>Electrical</b> Ratings:</h2>
      <div class="box">
        <table class="ratings">
          <tr><th>Model</th><th>Rated<br>Voltage (V)</th><th>Frequency<br>(Hz)</th><th>Rated<br>Current (A)</th><th>Rated<br>Wattage (W)</th><th>CCT<br>(K)</th><th>Lumens<br>(lm)</th></tr>
          <tr><td>QV043-YY-ZZ-U-T</td><td>120-277</td><td>50/60</td><td>0.45</td><td>30-45</td><td>4000</td><td>5400</td></tr>
          <tr><td>QV043-YY-ZZ-U-T</td><td>120-277</td><td>50/60</td><td>0.62</td><td>45-60</td><td>4000</td><td>7200</td></tr>
          <tr><td>QV043-YY-ZZ-U-T</td><td>120-277</td><td>50/60</td><td>0.85</td><td>60-80</td><td>4000</td><td>9600</td></tr>
          <tr><td>QV043-YY-ZZ-U-T</td><td>120-277</td><td>50/60</td><td>1.05</td><td>80-100</td><td>4000</td><td>12000</td></tr>
          <tr><td>QV043-YY-ZZ-U-T</td><td>120-277</td><td>50/60</td><td>1.25</td><td>100-120</td><td>4000</td><td>14400</td></tr>
          <tr><td>QV043-YY-ZZ-U-T</td><td>120-277</td><td>50/60</td><td>1.55</td><td>120-150</td><td>4000</td><td>18000</td></tr>
          <tr><td>QV043-YY-ZZ-U-T</td><td>120-277</td><td>50/60</td><td>1.85</td><td>150-180</td><td>4000</td><td>21600</td></tr>
          <tr><td>QV043-YY-ZZ-U-T</td><td>120-277</td><td>50/60</td><td>2.10</td><td>180-200</td><td>4000</td><td>24000</td></tr>
        </table>
      </div>
      <div class="brand footer-brand"><span class="dot"></span>Quorivanta</div>
      <div class="page-tab">Page 01</div>
    </article>

    <article class="page right inner">
      <h2 class="heading"><b>Nomenclature:</b></h2>
      <div class="box">
        <table class="nomen">
          <tr><td>Example:</td><td>QV</td><td>043</td><td>3H</td><td>CW</td><td>U</td><td>P</td><td>B</td></tr>
          <tr><td>Group:</td><td>xxx</td><td>YYY</td><td>ZZZ</td><td>CW</td><td>U</td><td>P</td><td>B</td></tr>
        </table>
        <table class="legend" style="margin-top:10px">
          <tr><th>Group</th><th>Description</th></tr>
          <tr><td>QV</td><td>Series name.</td></tr>
          <tr><td>XXX</td><td>Represents lamp wattage; may be any number, e.g. 043.</td></tr>
          <tr><td>YYY</td><td>Represents the optics model number.</td></tr>
          <tr><td>ZZZ</td><td>Represents colour temperature; may be CW - Cool White, NW - Neutral White, WW - Warm White.</td></tr>
          <tr><td>U</td><td>Represents input voltage is 120-277V.</td></tr>
          <tr><td>P</td><td>Represents dimming function; may be P - Photocell, D - DALI, Z - 0-10V.</td></tr>
          <tr><td>B</td><td>Represents lamp colour; may be G - Grey, B - Black, W - White.</td></tr>
        </table>
      </div>
      <h2 class="heading" style="margin-top:20px"><b>Lighting Distribution Types:</b></h2>
      <div class="types">
        <div class="type"><p>Type II Medium</p><div class="chart" role="img" aria-label="Polar light distribution chart, Type II Medium"></div></div>
        <div class="type"><p>Type III Medium</p><div class="chart" role="img" aria-label="Polar light distribution chart, Type III Medium"></div></div>
        <div class="type"><p>Type III Medium</p><div class="chart" role="img" aria-label="Iso-illuminance plot, Type III Medium"></div></div>
      </div>
      <div class="footer-url">www.quorivanta.com</div>
      <div class="page-tab">Page 02</div>
    </article>
  </section>

  <!-- pages 03-04 -->
  <section class="spread">
    <article class="page left inner">
      <svg class="corner" width="120" height="120" viewBox="0 0 120 120" aria-hidden="true"><polygon points="0,0 120,0 0,120" fill="var(--orange)"/></svg>
      <h2 class="model">QV043-YY-ZZ-U-D-T</h2>
      <p class="sub"><span>Performance Criteria</span> : LED Luminaire</p>
      <table class="spec">
        <tr><td class="k">Voltage</td><td class="d">Nominal input voltage range</td><td class="v">120-277 V</td></tr>
        <tr><td class="k">Input Power</td><td class="d">Maximum rated input power</td><td class="v">45 W</td></tr>
        <tr><td class="k">Lumen Output</td><td class="d">Initial delivered luminous flux</td><td class="v">5400 lm</td></tr>
        <tr><td class="k">Efficacy</td><td class="d">Min. system efficacy at 25°C</td><td class="v">120 lm/W</td></tr>
        <tr><td class="k">Power Factor</td><td class="d">At full rated load</td><td class="v">&gt; 0.95</td></tr>
        <tr><td class="k">THD</td><td class="d">Total harmonic distortion</td><td class="v">&lt; 15%</td></tr>
        <tr><td class="k">Lumen Maint.</td><td class="d">L70 rated life at 25°C</td><td class="v">&gt; 100,000 h</td></tr>
        <tr><td class="k">CCT</td><td class="d">Correlated colour temperature</td><td class="v">4000 K</td></tr>
        <tr><td class="k">Chromaticity Shift</td><td class="d">Shift over 6,000 hours</td><td class="v">&lt; 0.007</td></tr>
        <tr><td class="k">CRI</td><td class="d">Colour rendering index</td><td class="v">&gt; 70</td></tr>
        <tr><td class="k">IP</td><td class="d">Ingress protection, optical unit</td><td class="v">IP66</td></tr>
        <tr><td class="k">IK</td><td class="d">Impact resistance rating</td><td class="v">IK08</td></tr>
        <tr><td class="k">Weight</td><td class="d">Complete luminaire</td><td class="v">4.2 kg</td></tr>
        <tr><td class="k">EPA</td><td class="d">Effective projected area</td><td class="v">0.05 m²</td></tr>
        <tr><td class="k">Optical Distribution</td><td class="d">IES road lighting types</td><td class="v">Type II / III</td></tr>
        <tr><td class="k">Mounting</td><td class="d">Side entry, pole arm</td><td class="v">Ø42-60 mm</td></tr>
        <tr><td class="k">Surge Protection Device</td><td class="d">Line to earth rating</td><td class="v">10 kV</td></tr>
        <tr><td class="k">Control Interface</td><td class="d">NEMA 7-pin receptacle</td><td class="v">Optional</td></tr>
        <tr><td class="k">LED Driver</td><td class="d">Constant current, dimmable</td><td class="v">0-10 V</td></tr>
      </table>
      <div class="brand footer-brand"><span class="dot"></span>Quorivanta</div>
      <div class="page-tab">Page 03</div>
    </article>

    <article class="page right inner">
      <h2 class="model">QV043-YY-ZZ-U-D-T</h2>
      <p class="sub"><span>Certifications</span> : LED Luminaire</p>
      <table class="spec">
        <tr><td class="k">Safety</td><td class="d">Standard for luminaires, outdoor use</td><td class="v">Certified</td></tr>
        <tr><td class="k">FCC</td><td class="d">Part 15, Class A emissions</td><td class="v">Compliant</td></tr>
        <tr><td class="k">Dielectric Withstand</td><td class="d">Voltage test, 1 minute</td><td class="v">1500 V</td></tr>
        <tr><td class="k">Impact Resistance</td><td class="d">Test on optical cover</td><td class="v">IK08</td></tr>
        <tr><td class="k">Vibration</td><td class="d">Bridge and overpass rating</td><td class="v">3G</td></tr>
        <tr><td class="k">RoHS</td><td class="d">Hazardous substance directive</td><td class="v">Compliant</td></tr>
        <tr><td class="k">Salt Spray</td><td class="d">Coating test, 1000 hours</td><td class="v">Passed</td></tr>
        <tr><td class="k">Housing</td><td class="d">Die-cast aluminium alloy</td><td class="v">ADC12</td></tr>
        <tr><td class="k">Optical Material</td><td class="d">UV stabilised lens</td><td class="v">PC</td></tr>
        <tr><td class="k">Finish</td><td class="d">Polyester powder coat</td><td class="v">Grey</td></tr>
      </table>
      <p class="photos-title">Photos for two-module luminaire: “QV043-YY-ZZ-U-D-T”</p>
      <div class="photo-row">
        <div class="photo" role="img" aria-label="Two-module street luminaire, side view"></div>
        <div class="photo" role="img" aria-label="Two-module street luminaire, underside view showing LED modules"></div>
      </div>
      <div class="footer-url">www.quorivanta.com</div>
      <div class="page-tab">Page 04</div>
    </article>
  </section>

  <!-- pages 05-06 -->
  <section class="spread">
    <article class="page left inner">
      <svg class="corner" width="120" height="120" viewBox="0 0 120 120" aria-hidden="true"><polygon points="0,0 120,0 0,120" fill="var(--orange)"/></svg>
      <h2 class="model">QV043-YY-ZZ-U-D-T</h2>
      <p class="sub"><span>Performance Criteria</span> : LED Luminaire</p>
      <table class="spec">
        <tr><td class="k">Voltage</td><td class="d">Nominal input voltage range</td><td class="v">120-277 V</td></tr>
        <tr><td class="k">Input Power</td><td class="d">Maximum rated input power</td><td class="v">30 W</td></tr>
        <tr><td class="k">Lumen Output</td><td class="d">Initial delivered luminous flux</td><td class="v">3600 lm</td></tr>
        <tr><td class="k">Efficacy</td><td class="d">Min. system efficacy at 25°C</td><td class="v">120 lm/W</td></tr>
        <tr><td class="k">Power Factor</td><td class="d">At full rated load</td><td class="v">&gt; 0.95</td></tr>
        <tr><td class="k">THD</td><td class="d">Total harmonic distortion</td><td class="v">&lt; 15%</td></tr>
        <tr><td class="k">Lumen Maint.</td><td class="d">L70 rated life at 25°C</td><td class="v">&gt; 100,000 h</td></tr>
        <tr><td class="k">CCT</td><td class="d">Correlated colour temperature</td><td class="v">4000 K</td></tr>
        <tr><td class="k">Chromaticity Shift</td><td class="d">Shift over 6,000 hours</td><td class="v">&lt; 0.007</td></tr>
        <tr><td class="k">CRI</td><td class="d">Colour rendering index</td><td class="v">&gt; 70</td></tr>
        <tr><td class="k">IP</td><td class="d">Ingress protection, optical unit</td><td class="v">IP66</td></tr>
        <tr><td class="k">IK</td><td class="d">Impact resistance rating</td><td class="v">IK08</td></tr>
        <tr><td class="k">Weight</td><td class="d">Complete luminaire</td><td class="v">2.8 kg</td></tr>
        <tr><td class="k">EPA</td><td class="d">Effective projected area</td><td class="v">0.03 m²</td></tr>
        <tr><td class="k">Optical Distribution</td><td class="d">IES road lighting types</td><td class="v">Type II / III</td></tr>
        <tr><td class="k">Mounting</td><td class="d">Side entry, pole arm</td><td class="v">Ø42-60 mm</td></tr>
        <tr><td class="k">Surge Protection Device</td><td class="d">Line to earth rating</td><td class="v">10 kV</td></tr>
        <tr><td class="k">Control Interface</td><td class="d">NEMA 7-pin receptacle</td><td class="v">Optional</td></tr>
        <tr><td class="k">LED Driver</td><td class="d">Constant current, dimmable</td><td class="v">0-10 V</td></tr>
      </table>
      <div class="brand footer-brand"><span class="dot"></span>Quorivanta</div>
      <div class="page-tab">Page 05</div>
    </article>

    <article class="page right inner">
      <h2 class="model">QV043-YY-ZZ-U-D-T</h2>
      <p class="sub"><span>Certifications</span> : LED Luminaire</p>
      <table class="spec">
        <tr><td class="k">Safety</td><td class="d">Standard for luminaires, outdoor use</td><td class="v">Certified</td></tr>
        <tr><td class="k">FCC</td><td class="d">Part 15, Class A emissions</td><td class="v">Compliant</td></tr>
        <tr><td class="k">Dielectric Withstand</td><td class="d">Voltage test, 1 minute</td><td class="v">1500 V</td></tr>
        <tr><td class="k">Impact Resistance</td><td class="d">Test on optical cover</td><td class="v">IK08</td></tr>
        <tr><td class="k">Vibration</td><td class="d">Bridge and overpass rating</td><td class="v">3G</td></tr>
        <tr><td class="k">RoHS</td><td class="d">Hazardous substance directive</td><td class="v">Compliant</td></tr>
        <tr><td class="k">Salt Spray</td><td class="d">Coating test, 1000 hours</td><td class="v">Passed</td></tr>
        <tr><td class="k">Housing</td><td class="d">Die-cast aluminium alloy</td><td class="v">ADC12</td></tr>
        <tr><td class="k">Optical Material</td><td class="d">UV stabilised lens</td><td class="v">PC</td></tr>
        <tr><td class="k">Finish</td><td class="d">Polyester powder coat</td><td class="v">Grey</td></tr>
      </table>
      <p class="photos-title">Photos for one-module luminaire: “QV043-YY-ZZ-U-D-T”</p>
      <div class="photo-row">
        <div class="photo" role="img" aria-label="One-module street luminaire, top view"></div>
        <div class="photo" role="img" aria-label="One-module street luminaire, underside view showing LED module"></div>
      </div>
      <div class="footer-url">www.quorivanta.com</div>
      <div class="page-tab">Page 06</div>
    </article>
  </section>

</main>
</body>
</html>
```